The name of the company is Kestrel Rehab buying foreclosed homes and remodeling

A sleek classy card. It’s a home remodel and house flip company. Something mostly black with dark gray and red in color . Something with two f”s as a logo on front as shown in pictures. Kind of just let you guys run with it . I left a few pictures that should help
You guys get an idea of what I thought was good also left all the information for back of the card

Target Market(s)

Home remodel consumers

Industry/Entity Type

Construction Company

Contact Information for Business Card

All details are on photo

Font styles to use
Decorative

Colors

Designer to choose colors to be used in the design.

Requirements
Must have
• Name of company on front. Kestrel Rehab
Nice to have
• Up to you guys I trust you
Should not have
• Not sure

```html
<!DOCTYPE html>
<html lang="en">
<head>
<meta charset="UTF-8">
<title>Kestrel Rehab – Business Card</title>
<link href="https://fonts.googleapis.com/css2?family=Roboto:wght@400;700&display=swap" rel="stylesheet">
<style>
  :root {
    --canvas: #2b2b2e;
    --card: #1f2123;
    --card-edge: #2c2f31;
    --ink: #f2f2f2;
    --ink-soft: #d8d8d8;
    --ghost: #161718;
    --rule: #bdbdbd;
  }
  * { margin: 0; padding: 0; box-sizing: border-box; }
  html, body { width: 1200px; height: 800px; overflow: hidden; }
  body {
    background: var(--canvas);
    font-family: "Roboto", Arial, sans-serif;
    color: var(--ink);
    display: flex;
    align-items: center;
    justify-content: center;
    gap: 40px;
  }
  .card {
    position: relative;
    width: 540px;
    height: 309px;
    background: var(--card);
    border: 1px solid var(--card-edge);
    border-radius: 4px;
    box-shadow: 0 18px 40px rgba(0,0,0,.45);
    overflow: hidden;
  }
  .brand {
    display: flex;
    align-items: center;
    gap: 10px;
    font-weight: 700;
    color: var(--ink);
    white-space: nowrap;
  }
  .brand-mark {
    width: 14px;
    height: 14px;
    background: var(--ink);
  }
  /* Front */
  .card-front .brand {
    position: absolute;
    top: 100px;
    left: 0;
    right: 0;
    justify-content: center;
    font-size: 34px;
  }
  .card-front .tagline {
    position: absolute;
    left: 0;
    right: 0;
    top: 200px;
    text-align: center;
    font-size: 13px;
    font-weight: 700;
    letter-spacing: .2px;
    color: var(--ink);
  }
  /* Back */
  .card-back .brand {
    position: absolute;
    top: 34px;
    right: 40px;
    font-size: 24px;
  }
  .ghost-name {
    position: absolute;
    right: 34px;
    top: 96px;
    font-size: 44px;
    line-height: 1;
    font-weight: 700;
    text-align: right;
    color: var(--ghost);
    white-space: nowrap;
  }
  .contact {
    position: absolute;
    left: 38px;
    bottom: 30px;
  }
  .contact .person {
    font-size: 21px;
    font-weight: 700;
    padding-bottom: 6px;
    border-bottom: 1px solid var(--rule);
    width: 280px;
    margin-bottom: 10px;
  }
  .contact ul { list-style: none; }
  .contact li {
    display: flex;
    align-items: center;
    gap: 10px;
    font-size: 13px;
    color: var(--ink-soft);
    line-height: 21px;
  }
  .contact svg { width: 12px; height: 12px; fill: var(--ink-soft); flex: none; }
  .contact .square { width: 10px; height: 10px; border: 1.5px solid var(--ink-soft); margin: 0 1px; flex: none; }
  .contact .web {
    margin-top: 8px;
    font-size: 13px;
    letter-spacing: 4px;
    color: var(--ink-soft);
  }
  .contact .web b { font-weight: 700; color: var(--ink); }
</style>
</head>
<body>
  <section class="card card-front">
    <div class="brand"><span class="brand-mark"></span>Kestrel Rehab</div>
    <p class="tagline">Central Contractor | Home | Remodel | Concrete Alternatives</p>
  </section>

  <section class="card card-back">
    <div class="ghost-name" aria-hidden="true">Kestrel<br>Rehab</div>
    <div class="brand"><span class="brand-mark"></span>Kestrel Rehab</div>
    <div class="contact">
      <p class="person">Daniel Okafor JR</p>
      <ul>
        <li>
          <svg viewBox="0 0 24 24" aria-hidden="true"><path d="M6.6 10.8a15.1 15.1 0 0 0 6.6 6.6l2.2-2.2c.3-.3.7-.4 1-.2 1.1.4 2.3.6 3.6.6.6 0 1 .4 1 1V20c0 .6-.4 1-1 1A17 17 0 0 1 3 4c0-.6.4-1 1-1h3.5c.6 0 1 .4 1 1 0 1.3.2 2.5.6 3.6.1.3 0 .7-.2 1z"/></svg>
          9101-555-0142
        </li>
        <li>
          <svg viewBox="0 0 24 24" aria-hidden="true"><path d="M2 5h20v14H2z M3 6l9 7 9-7" fill="none" stroke="#d8d8d8" stroke-width="2"/></svg>
          dokaforjr@mailbox.com
        </li>
        <li><span class="square"></span>Kestrel_Rehab_</li>
      </ul>
      <p class="web">www.<b>kestrelrehab</b>.com</p>
    </div>
  </section>
</body>
</html>
```